Need a clean & modern homepage for an education site + opportunity for longer term work

Thanks for viewing our project. We are excited about this new website and we hope that we might build a relationship with designers as we work on this project. I provided quite a few details and requirements to help you more quickly create a design that meets our needs.
Who we are:
We are a website that discusses the importance of college accreditation and provides a directory of college programs.
What we need:
A homepage that meets the below requirements and is inspired by the examples provided
Definition of accredited:
ac·cred·it·ed [uh-kred-i-tid] adj.
1. officially recognized as meeting the essential requirements, as of academic excellence: accredited schools.
2. provided with official credentials, as by a government: an accredited diplomatic representative.
3. accepted as authoritative: an accredited theory.
Overall look and feel for the homepage:
- Clean, simple and modern
- Limited (or zero) pictures
- Utilize color blocks with text
- A trend seems to be longer vertical length homepages with lots of whitespace. I generally like this trend as long as the page is not way to tall.
Inspirations: Sites that have a similar look and feel to what I need.
http://lernvista.org/
http://www.campusmetrix.com/colleges/orlen-university/
http://quietmarrow.org/
http://www.velmoratalent.com/
http://www.pluvo.com/
http://sketches.zumo.com/
Items to be included on the homepage. Details below on each item.
- Top navigation
- Logo: Please leave a blank area for a logo. The logo has not been designed.
- Simple graphic/color block at the top that highlights a definition of “Accredited” – the definition should be formatted like it is being copy/pasted from a dictionary.
- Space for a video and small (50 word) written description of the video. You can use placeholder text.
- One section with 3 Paragraphs of content (each paragraph around 100 words) with a header at the top. You can use placeholder text but please create the formatting. At the end of the 3 paragraphs please have a “Read More” Note this shouldn't be 3 separate paragraphs with three read mores - it is 3 paragraphs with one read more at the end.
- An area with the header “Search Colleges by State” that has anchor text links to all 50 states.
Top navigation:
- Home
- States – with a subnav dropdown that includes all 50 US states.
- Programs – with a subnav dropdown that includes program titles (list below)
- Degrees - with a subnav dropdown that includes 5 degree levels (list below)
- Accreditation – no subnav
- Rankings – no subnav
- Resources – no subnav
Footer
- Link to about us, privacy, and a copyright www.url.com
Programs List for sub navigation
Accounting
Art
Bible
Business
Criminal Justice
Design
Engineering
English
Law
LPN to RN
Management
Math
MBA
MPH
Medical Assisting
Military
Nursing
Occupational Therapy
Paralegal
Psychology
Pharmacy
RN to BSN
Radiology
Social Work
Sonography
Degrees list for sub navigation
Certificate
Associate
Bachelors
Masters
PhD
Thanks so much - looking forward to working with you!

```html
<!DOCTYPE html>
<html lang="en">
<head>
<meta charset="utf-8">
<title>Accredited – Homepage</title>
<link href="https://fonts.googleapis.com/css2?family=Raleway:wght@300;400;600;700&family=Roboto+Slab:wght@300;400;700&display=swap" rel="stylesheet">
<style>
:root{
  --navy:#0b1b3f;
  --blue:#1e6fff;
  --teal:#0cc6a8;
  --red:#f2354f;
  --grey-block:#efefef;
  --grey-dark:#e2e2e2;
  --text:#5a5a5a;
  --white:#ffffff;
}
*{margin:0;padding:0;box-sizing:border-box}
html,body{width:681px;height:1200px;overflow:hidden;background:var(--white)}
body{position:relative;font-family:'Raleway',sans-serif;color:var(--text)}
a{color:inherit;text-decoration:none}

.logo-slot{position:absolute;left:44px;top:48px;width:185px;height:79px;background:var(--grey-block);
  display:flex;align-items:center;justify-content:center;font-size:10px;letter-spacing:1.5px;color:#aaa}

.definition{position:absolute;left:318px;top:48px;width:363px;height:82px}
.definition svg{position:absolute;inset:0}
.definition-text{position:absolute;left:55px;top:10px;width:274px;font-family:'Roboto Slab',serif;
  font-size:8.6px;line-height:11.4px;color:#8a8a8a;text-align:justify;font-weight:300}
.definition-text .word{font-weight:700;color:var(--navy);font-size:10px}
.definition-text b{color:var(--navy);font-weight:700}

.main-nav{position:absolute;left:0;top:176px;width:681px;height:27px;background:var(--navy);z-index:3}
.main-nav ul{list-style:none;display:flex;height:100%;padding-left:37px}
.main-nav li{height:100%;padding:0 9px;display:flex;align-items:center;color:var(--white);
  font-weight:700;font-size:8.4px;letter-spacing:.3px}
.main-nav li.active{background:var(--blue)}
.social{position:absolute;right:36px;top:0;height:27px;display:flex;align-items:center;gap:6px}
.social span{display:flex;align-items:center;gap:2px;font-size:6.5px;font-weight:600;color:var(--white)}
.social i{display:block;width:6px;height:6px;border-radius:50%;background:var(--white)}

.intro-title{position:absolute;left:46px;top:252px;font-size:21px;line-height:26px;font-weight:300;color:var(--blue);white-space:nowrap}
.dropdown{position:absolute;left:137px;top:203px;width:383px;height:99px;background:rgba(255,255,255,.88);
  display:flex;padding:8px 0 0 9px;z-index:2}
.dropdown ul{list-style:none;width:97px;font-size:7.3px;line-height:12px;color:#777;white-space:nowrap}
.dropdown ul:nth-child(2){width:92px}
.dropdown ul:nth-child(4){padding-top:2px}
.intro-copy{position:absolute;left:46px;top:320px;width:260px;font-size:9.6px;line-height:14.2px;color:var(--text);white-space:nowrap}
.btn{position:absolute;height:22px;width:75px;font-family:'Roboto Slab',serif;font-size:10.5px;
  display:flex;align-items:center;justify-content:center}
.btn::after{content:"";position:absolute;right:0;top:0;border-style:solid;border-width:0 8px 8px 0}
.btn-dark{left:46px;top:416px;background:var(--navy);color:var(--white)}
.btn-dark::after{border-color:transparent #d9dde6 #9aa3b6 transparent}

.video{position:absolute;left:318px;top:253px;width:328px;height:185px;z-index:1;
  background:linear-gradient(100deg,#cfc9c2 0%,#8d8a86 30%,#2b2a2c 55%,#4a4644 75%,#b9b3ac 100%)}
.video svg{position:absolute;left:157px;top:78px}

.cards{position:absolute;left:35px;top:469px;display:flex;gap:15px}
.card{position:relative;width:194px;height:347px;color:var(--white);padding:14px 13px 0 11px}
.card-teal{background:linear-gradient(135deg,#0fb89e 0%,#0cc6a8 40%,#11d0b3 100%)}
.card-red{background:linear-gradient(135deg,#e02943 0%,#f2354f 40%,#f5405a 100%)}
.card-blue{background:linear-gradient(135deg,#165fe6 0%,#1e6fff 40%,#2a78ff 100%)}
.card h2{font-weight:400;font-size:15.5px;line-height:21px;margin-bottom:12px}
.card p{font-size:8.2px;line-height:12.6px;margin-bottom:12.6px}
.card p b{font-weight:700}
.card .btn{left:14px;top:313px;background:var(--white)}
.card-teal .btn{color:var(--teal)}
.card-red .btn{color:var(--red)}
.card-blue .btn{color:var(--blue)}
.card .btn::after{border-color:transparent var(--navy) rgba(0,0,0,.12) transparent}

.states{position:absolute;left:0;top:845px;width:681px;height:298px;background:var(--navy)}
.states-map{position:absolute;left:28px;top:20px;width:412px;height:258px;border-radius:12px;
  background:radial-gradient(ellipse at 50% 50%,#16306a 0%,#11275a 55%,var(--navy) 100%)}
.states-label{position:absolute;left:466px;top:26px;font-family:'Roboto Slab',serif;font-size:8.6px;color:var(--blue);
  display:flex;align-items:center;gap:6px}
.states-label i{width:5px;height:5px;border-radius:50%;background:var(--blue);display:block}
.states h2{position:absolute;left:468px;top:53px;font-weight:400;font-size:15.5px;line-height:21px;color:var(--white);white-space:nowrap}
.states .btn{left:469px;top:159px;background:var(--white);color:var(--navy)}
.states .btn::after{border-color:transparent var(--navy) var(--blue) transparent}
.states-copy{position:absolute;left:469px;top:202px;font-size:8.3px;line-height:12.4px;color:var(--white);white-space:nowrap}

.site-footer{position:absolute;left:0;top:1166px;width:681px;text-align:center;font-family:'Roboto Slab',serif;
  font-size:8.6px;color:var(--navy)}
.site-footer span{margin:0 5px}
</style>
</head>
<body>

<header>
  <div class="logo-slot">LOGO</div>
  <div class="definition">
    <svg width="363" height="82" viewBox="0 0 363 82">
      <polygon points="0,0 363,0 363,82 0,82 32,41" fill="var(--grey-block)"/>
      <polygon points="0,0 32,41 0,82" fill="var(--grey-dark)"/>
    </svg>
    <p class="definition-text"><span class="word">ac·cred·it·ed</span> [uh-kred-i-tid] <i>adj</i> <b>1.</b> officially recognized as meeting the essential requirements, as of academic excellence: accredited schools. <b>2.</b> provided with official credentials, as by a government: an accredited diplomatic representative. <b>3.</b> accepted as authoritative: an accredited theory.</p>
  </div>
</header>

<nav class="main-nav">
  <ul>
    <li>HOME</li>
    <li>STATES •</li>
    <li class="active">PROGRAMS •</li>
    <li>DEGREES •</li>
    <li>ACCREDITATION</li>
    <li>RANKINGS</li>
    <li>RESOURCES</li>
  </ul>
  <div class="social">
    <span><i></i>Friendloop</span>
    <span><i></i>Chirpnet</span>
  </div>
</nav>

<section class="intro">
  <h1 class="intro-title">Accreditation Unique<br>Landing Page</h1>
  <div class="dropdown">
    <ul><li>Accounting</li><li>Art</li><li>Bible</li><li>Business</li><li>Criminal Justice</li><li>Design</li><li>Education</li></ul>
    <ul><li>Engineering</li><li>English</li><li>Law</li><li>LPN to RN</li><li>Management</li><li>Math</li><li>MBA</li></ul>
    <ul><li>MPH</li><li>Medical Assisting</li><li>Military</li><li>Nursing</li><li>Occupational Therapy</li><li>Paralegal</li><li>Psychology</li></ul>
    <ul><li>Pharmacy</li><li>RN to BSN</li><li>Radiology</li><li>Social Work</li><li>Sonography</li></ul>
  </div>
  <p class="intro-copy">Lorem ipsum dolor sit amet, conse ctetur adipisicel,<br>sed eiusmod tempor incidunt ut labore et dolore<br>magna aliqua. Ut enim ad minim veniam, quis nstrd<br>exer citation ullamco laboris nisi ut aliquid ex ea<br>commodi consequat. Quis aute iure rep henderit in<br>voluptate velit esse cillum.</p>
  <a class="btn btn-dark" href="#">read more</a>
  <div class="video" role="img" aria-label="Video still: two students looking at a tablet together">
    <svg width="22" height="28" viewBox="0 0 22 28"><polygon points="0,0 22,14 0,28" fill="#fff"/></svg>
  </div>
</section>

<section class="cards">
  <article class="card card-teal">
    <h2>Accreditated Aliquero Landing Page</h2>
    <p>Lorem ipsum dolor sit amet, con secte tur adipisici elit, sed eiusmod tempor incidunt ut labore <b>et dolore magna</b> aliqua. Ut enim ad minim veniam, quis nostrud exer citation ullamco laboris nisi ut aliquid ex ea commodi consequat sed eiusmod tempor incidunt ut labore et dolore magna aliqua.</p>
    <p>Ut enim ad minim. Lorem ipsum dolor sit amet, con sectetur <b>adipisici elit, sed eiusmod tempor incidunt</b> ut labore et dolore magna aliqua.<br>Ut enim ad minim veniam, quis nostrud exer citation ullamco laboris nisi ut alirquid ex ea commodi <b>consequat</b> sed eiusmod tempor incidunt ut labore et dolore magna aliqua. Ut enim ad minim.</p>
    <a class="btn" href="#">read more</a>
  </article>
  <article class="card card-red">
    <h2>Incidunt Minimere Venieme</h2>
    <p>Lorem ipsum dolor sit amet, con secte tur adipisici elit, sed eiusmod tempor incidunt ut labore et dolore magnantes.</p>
    <p><b>Aliqua ut enim</b> ad <b>minim veniadrm</b>, quis nostrud exer citation ullamco.</p>
    <p>Laboris nisi ut aliquid ex ea commodi consequat <b>sed eiusmod tempor incidunt ut labore et dolore</b> magna aliqua.<br>Ut enim ad minim. Lorem ipsum dolor sit amet, con sectetur adipisici elit, sed eiusmod tempor incidunt ut labore et dolore magna aliqua. Ut enim ad minim veniam, quis nostrud exer citation ulla mco laboris nisi ut alirquid ex ea commo di consequat sed <b>eiusmod tempor incidunt ut labore</b> et dolore yagna liqua.</p>
    <a class="btn" href="#">read more</a>
  </article>
  <article class="card card-blue">
    <h2>Commodi Leborenet Consequant</h2>
    <p>Lorem ipsum dolor sit amet, con secte tur <b>adipisici</b> elit, <b>sed eiusmod</b> tempor <b>incidunt</b> ut labore et dolore magna aliqua. Ut enim ad <b>minim veniam</b>, quis nostrud exer citation ullamco. Laboris nisi ut aliquid ex ea commodi consequat.</p>
    <p>Sed eiusmod tempor incidunt ut laborte et dolore magna aliqua. Ut enim ader minim. Lorem ipsum dolor sit ametcotn sectetur adipisici elit, <b>sed eiusmod rfe tempor incidunt</b> utlabore et doloreeroto magna aliqua.</p>
    <p>Ut enim ad <b>minim veniam</b>, quis nostrud exer citation ulla <b>mco laboris</b> nisi ut <b>alirquid</b> ex ea commo di consequat sed eiusmod tempor incidunt.</p>
    <a class="btn" href="#">read more</a>
  </article>
</section>

<section class="states">
  <div class="states-map" role="img" aria-label="Map of the United States with state borders and dots marking colleges"></div>
  <p class="states-label"><i></i>lorem im sit solorem desint</p>
  <h2>SEARCH COLLEGES<br>BY THE STATES<br>Lorem ipsum dor st<br>amet, con secter.</h2>
  <a class="btn" href="#">full list</a>
  <p class="states-copy">Ut enim ad minim. Lorem ipsum<br>dolor sit amet, con sectetur <b>adipisici</b><br><b>elit, sed eiusmod tempor incidunt</b><br>ut labore et dolore magna aliqua.</p>
</section>

<footer class="site-footer">
  <a href="#">about us</a><span>|</span><a href="#">privacy</a><span>|</span>copyright © www.url.com
</footer>

</body>
</html>
```